Design a banner for a home page shop

I need someone who can design a banner for a photographic website.
The website has 2 main section shop and blog. You can advertize what u want. You can decide the images.

I need creative people.

I will pay the best one.

```html
<!DOCTYPE html>
<html lang="en">
<head>
<meta charset="UTF-8">
<title>Design Banners for Photographic Website</title>
<link href="https://fonts.googleapis.com/css2?family=Lato:wght@700;900&family=Montserrat:wght@600;800&display=swap" rel="stylesheet">
<style>
  :root {
    --brand-red: #b0121a;
    --stage-light: #e6e6e6;
    --stage-dark: #8f8f8f;
    --banner-black: #0b0b0b;
    --banner-stripe: #0f0f0f;
    --accent-red: #e3261c;
    --accent-orange: #f2a31b;
    --text-white: #ffffff;
    --button-bg: #1b1b1b;
    --button-border: #5a3a1a;
    --product-dark: #1c1c1c;
    --product-mid: #4a4a4a;
    --product-light: #8a8a8a;
  }
  * { margin: 0; padding: 0; box-sizing: border-box; }
  html, body { width: 1200px; height: 605px; overflow: hidden; }
  body {
    position: relative;
    background: radial-gradient(ellipse 70% 85% at 50% 40%, var(--stage-light) 0%, #c4c4c4 55%, var(--stage-dark) 100%);
    font-family: "Lato", sans-serif;
  }
  .title-bar {
    position: absolute; left: 61px; top: 36px; width: 1071px; height: 61px;
    background: var(--brand-red); border-radius: 4px;
    display: flex; align-items: center; justify-content: center;
  }
  .title-bar h1 {
    color: var(--text-white); font-weight: 900; font-size: 29px; letter-spacing: 0.3px;
  }
  .footer-band {
    position: absolute; left: 0; top: 543px; width: 1200px; height: 62px;
    background: var(--brand-red);
  }
  .banner-label {
    position: absolute; top: 208px; width: 169px; height: 36px;
    background: var(--brand-red); color: var(--text-white);
    font-weight: 900; font-size: 21px;
    display: flex; align-items: center; justify-content: center;
  }
  .banner-label.first { left: 283px; }
  .banner-label.second { left: 743px; }
  .promo-banner {
    position: absolute; top: 269px; width: 389px; height: 159px;
    background: repeating-linear-gradient(135deg, var(--banner-black) 0 18px, var(--banner-stripe) 18px 36px);
    box-shadow: 0 6px 10px rgba(0,0,0,0.3);
    overflow: hidden;
  }
  .promo-banner.first { left: 173px; }
  .promo-banner.second { left: 631px; }
  .promo-banner h2 {
    position: absolute; left: 9px; top: 45px;
    font-family: "Montserrat", sans-serif; font-weight: 800; font-size: 18px; letter-spacing: 0.4px;
  }
  .promo-banner.first h2 { color: var(--accent-red); }
  .promo-banner.second h2 { color: var(--accent-orange); }
  .promo-banner p {
    position: absolute; left: 9px; top: 67px; width: 165px;
    color: var(--text-white); font-family: "Montserrat", sans-serif; font-weight: 600;
    font-size: 8.5px; line-height: 10.5px;
  }
  .shop-button {
    position: absolute; left: 9px; top: 99px; width: 101px; height: 19px;
    background: var(--button-bg); border: 1px solid var(--button-border); border-radius: 2px;
    display: flex; align-items: center; gap: 5px; padding-left: 5px;
    font-family: "Montserrat", sans-serif; font-weight: 600; font-size: 8.5px;
  }
  .promo-banner.first .shop-button { color: var(--accent-red); }
  .promo-banner.second .shop-button { color: var(--accent-orange); }
  .shop-button .caret { margin-left: auto; padding: 0 5px; border-left: 1px solid #333; height: 100%; display: flex; align-items: center; }
  .product-photo {
    position: absolute;
    border-radius: 10px;
    background:
      radial-gradient(ellipse 45% 40% at 30% 50%, var(--product-light) 0%, var(--product-mid) 35%, transparent 70%),
      radial-gradient(ellipse 60% 55% at 55% 45%, var(--product-mid) 0%, var(--product-dark) 70%),
      var(--product-dark);
  }
  .promo-banner.first .product-photo { left: 204px; top: 8px; width: 163px; height: 128px; }
  .promo-banner.second .product-photo { left: 212px; top: 10px; width: 146px; height: 126px; }
  .floor-glow {
    position: absolute; bottom: 0; height: 26px;
    background: radial-gradient(ellipse 50% 60% at 50% 30%, rgba(120,120,120,0.45), transparent 75%);
  }
  .promo-banner.first .floor-glow { left: 190px; width: 190px; }
  .promo-banner.second .floor-glow { left: 200px; width: 170px; }
</style>
</head>
<body>
  <header class="title-bar"><h1>DESIGN BANNERS FOR PHOTOGRAPHIC WEBSITE</h1></header>

  <div class="banner-label first">BANNER-1</div>
  <div class="banner-label second">BANNER-2</div>

  <section class="promo-banner first">
    <h2>PHOTOGRAPHY</h2>
    <p>Lorem Ipsum is simply dummy text of the printing and typesetting industry.</p>
    <div class="shop-button">
      <svg width="11" height="10" viewBox="0 0 11 10" fill="none" stroke="currentColor" stroke-width="1.3"><path d="M0.5 1h2l1.5 5h5.5l1-3.5H3.3"/><circle cx="4.5" cy="8.5" r="0.9" fill="currentColor"/><circle cx="8.5" cy="8.5" r="0.9" fill="currentColor"/></svg>
      <span>SHOP NOW!</span>
      <span class="caret"><svg width="6" height="4" viewBox="0 0 6 4"><path d="M0 0h6L3 4z" fill="currentColor"/></svg></span>
    </div>
    <div class="floor-glow"></div>
    <div class="product-photo" role="img" aria-label="Professional cinema camera with a large lens, side view"></div>
  </section>

  <section class="promo-banner second">
    <h2>PHOTOGRAPHY</h2>
    <p>Lorem Ipsum is simply dummy text of the printing and typesetting industry.</p>
    <div class="shop-button">
      <svg width="11" height="10" viewBox="0 0 11 10" fill="none" stroke="currentColor" stroke-width="1.3"><path d="M0.5 1h2l1.5 5h5.5l1-3.5H3.3"/><circle cx="4.5" cy="8.5" r="0.9" fill="currentColor"/><circle cx="8.5" cy="8.5" r="0.9" fill="currentColor"/></svg>
      <span>SHOP NOW!</span>
      <span class="caret"><svg width="6" height="4" viewBox="0 0 6 4"><path d="M0 0h6L3 4z" fill="currentColor"/></svg></span>
    </div>
    <div class="floor-glow"></div>
    <div class="product-photo" role="img" aria-label="Professional DSLR camera with lens, front three-quarter view"></div>
  </section>

  <div class="footer-band"></div>
</body>
</html>
```